Kitesurf Weather Forecast Application Needs an Advertising Banner

We need an Advertising Banner for our iOS Kitesurf Weather Forecast Application. The application name is GustMapper and you can download it from the Zelvo Mart.

https://store.zelvomart.example/app/gustmapper-sail-gust-and-sky-outlook/id840213957?mt=8

The banner should have the logo of our application, which can be either found from the zelvo mart or uploaded on this post. It should describe what our app does with either words or graphic story. GustMapper is a weather forecast application for Kitesurfers. As the banner is small, animated gifs will also be considered.

We need the following sizes 320x50 and 728x90. The banner will be uploaded to quarnix. Quarnix accepts images in PNG, JPEG and GIF. We want it in one of the formats that can be uploaded to QuarNix and vector .ai so we can make changed if necessary in the future.

On tap the banner will open Zelvo Mart on the user's device and present GustMapper.

06/09. I added a screenshot from an application that the banner will be added. The screenshot is from an Velonet 4 Max (it is from a big device). The red area on the bottom is where the advert will go and it should be readable.

Target Market(s)

Banner will be displayed in other iOS Applications. One of them is Tidal Sum Tool https://store.zelvomart.example/us/app/tidal-sum-tool/id305927184?mt=8

Industry/Entity Type

Advertising

Font styles to use
Other font styles liked:
• San Francisco

Requirements
Must have
• GustMapper logo and communicate a clear message on what the application does. GustMapper is a weather forecast application for Kitesurfers. If you want to find more information please visit the ZelvoMart link provided.
Nice to have
• Animated gif will be nice to have, as the banner is small and it maybe difficult to communicate the message required.
Should not have
• We prefer something minimal and along the lines of our application design.

```html
<!DOCTYPE html>
<html lang="en">
<head>
<meta charset="utf-8">
<title>GustMapper Ad Banner</title>
<link rel="stylesheet" href="https://fonts.googleapis.com/css2?family=Arimo:wght@400;700&display=swap">
<style>
  :root{
    --navy:#1c2a86;
    --navy-deep:#16226e;
    --sky-light:#cfe6f7;
    --sky-mid:#7fb6e3;
    --sky-deep:#3f7ec4;
    --white:#ffffff;
    --ink:#1b2a6b;
    --badge:#111111;
    --badge-edge:#8a8a8a;
    --box-fill:#e9f3fb;
  }
  *{box-sizing:border-box;margin:0;padding:0}
  html,body{width:1200px;height:148px;overflow:hidden;background:var(--white)}
  .banner{
    position:relative;width:1200px;height:148px;overflow:hidden;
    background:linear-gradient(90deg,var(--navy-deep) 0%,var(--navy) 55%,#24379a 100%);
    font-family:"Arimo",Arial,sans-serif;color:var(--white);
  }
  .sky-photo{
    position:absolute;top:0;left:560px;width:640px;height:148px;
    background:linear-gradient(100deg,rgba(63,126,196,0) 0%,var(--sky-deep) 28%,var(--sky-mid) 55%,var(--sky-light) 100%);
    clip-path:polygon(18% 0,100% 0,100% 100%,0 100%);
  }
  .feature{position:absolute;text-align:center;font-size:15px;line-height:20px;transform:translateX(-50%);white-space:nowrap}
  .feature .title{display:flex;align-items:center;justify-content:center;gap:6px}
  .icon{display:block}
  .weekly{left:119px;top:22px}
  .live{left:119px;top:82px}
  .custom{left:356px;top:14px}
  .map{left:359px;top:90px}
  .detailed{left:593px;top:30px}
  .store-badge{position:absolute;top:15px;height:32px;background:var(--badge);border:1.5px solid var(--badge-edge);border-radius:6px}
  .store-badge.zelvo{left:926px;width:90px}
  .store-badge.pexa{left:1030px;width:90px}
  .app-card{
    position:absolute;left:888px;top:66px;width:266px;height:64px;
    background:var(--box-fill);border:2px solid var(--ink);
    display:flex;align-items:center;gap:8px;padding:0 7px;
  }
  .app-mark{width:48px;height:48px;background:var(--ink);flex:none}
  .app-name{color:var(--ink);font-weight:700;font-size:17px;line-height:21px;text-align:center;flex:1;white-space:nowrap}
  .corner-icon{position:absolute;left:1138px}
</style>
</head>
<body>
<div class="banner">
  <div class="sky-photo" role="img" aria-label="Kitesurfer flying a kite against a bright cloudy blue sky"></div>

  <div class="feature weekly">
    <div class="title">
      <svg class="icon" width="26" height="18" viewBox="0 0 26 18"><path d="M6 16h14a5 5 0 0 0 0-10 7 7 0 0 0-13 1 4.5 4.5 0 0 0-1 9z" fill="none" stroke="#fff" stroke-width="1.8"/></svg>
      <span>Weekly Forecast</span>
    </div>
    <div>Showing only Kiteable Spots</div>
  </div>

  <div class="feature live">
    <div class="title">
      <svg class="icon" width="12" height="22" viewBox="0 0 12 22"><rect x="4" y="1" width="4" height="14" rx="2" fill="none" stroke="#fff" stroke-width="1.5"/><circle cx="6" cy="17" r="4" fill="#fff"/></svg>
      <span>Live Weather</span>
    </div>
    <div>Check Out Live Stations</div>
  </div>

  <div class="feature custom">
    <div class="title">
      <svg class="icon" width="26" height="26" viewBox="0 0 26 26" stroke="#fff" stroke-width="2" stroke-linecap="round"><path d="M13 2v22M3.5 7.5l19 11M3.5 18.5l19-11"/><path d="M10 4l3 3 3-3M10 22l3-3 3 3"/></svg>
    </div>
    <div>Customized Forecast for</div>
    <div>KiteSurfers</div>
  </div>

  <div class="feature map">
    <div class="title">
      <svg class="icon" width="18" height="18" viewBox="0 0 18 18" stroke="#fff" stroke-width="1.6" stroke-linecap="round"><circle cx="9" cy="9" r="4" fill="#fff"/><path d="M9 1v2M9 15v2M1 9h2M15 9h2M3.3 3.3l1.4 1.4M13.3 13.3l1.4 1.4M3.3 14.7l1.4-1.4M13.3 4.7l1.4-1.4"/></svg>
      <span>Weather on Map</span>
    </div>
    <div>Get Forecasr abd Live Data</div>
  </div>

  <div class="feature detailed">
    <div class="title">
      <svg class="icon" width="34" height="34" viewBox="0 0 34 34"><path d="M8 18h18a6 6 0 0 0 0-12 9 9 0 0 0-17 1 5.5 5.5 0 0 0-1 11z" fill="#fff"/><path d="M11 23l-2 5M18 23l-2 5M25 23l-2 5" stroke="#fff" stroke-width="2" stroke-linecap="round"/></svg>
    </div>
    <div>Detailed Weather</div>
    <div>See Hourly Forecast &amp; Live</div>
  </div>

  <div class="store-badge zelvo" aria-label="Zelvo Mart"></div>
  <div class="store-badge pexa" aria-label="Pexa Shelf"></div>

  <svg class="corner-icon" style="top:14px" width="40" height="32" viewBox="0 0 40 32"><circle cx="26" cy="10" r="6" fill="none" stroke="#fff" stroke-width="2"/><path d="M8 28h20a6 6 0 0 0 0-12 8 8 0 0 0-15 1 5.5 5.5 0 0 0-5 11z" fill="#fff"/></svg>

  <div class="app-card">
    <div class="app-mark" aria-hidden="true"></div>
    <div class="app-name">GustMapper Weather<br>Forecast Application</div>
  </div>

  <svg class="corner-icon" style="top:98px;left:1168px" width="28" height="20" viewBox="0 0 28 20"><path d="M6 18h15a5.5 5.5 0 0 0 0-11 7.5 7.5 0 0 0-14 1 5 5 0 0 0-1 10z" fill="#fff"/></svg>
</div>
</body>
</html>
```